Retractable Banner Design for Willowbrook Critters Florida Rebrand

We need a retractable banner design for our market booth. I absolutely love our old banner design and would like to keep it clean and similar but more on theme with the new brand with the new colors. Full brand guide attached. Our slogan we would like to include is "professional pet care for when you can't be there" (dog walking & pet sitting).
Our services we would like to include is: Extended Visits, Pop In Visits, Dog Walking, Pet Taxi, Travel & Adventure Hikes.
We offer: Discounts for First Responders, Teachers, & Military
I would like to use elements from the brand as well as the colors. Include the website www.willowbrookcritters.net somewhere

```html
<!DOCTYPE html>
<html lang="en">
<head>
<meta charset="utf-8">
<title>Willowbrook Critters Florida – Retractable Banner</title>
<link rel="stylesheet" href="https://fonts.googleapis.com/css2?family=Fraunces:opsz,wght@9..144,700;9..144,900&family=Playfair+Display:wght@700&family=Noto+Sans:wght@500;700;800&display=swap">
<style>
  :root {
    --cream: #f4ede3;
    --ink: #173f50;
    --teal: #1b6783;
    --pink: #e13aa8;
    --yellow: #ebcd63;
    --ring: #f2e2a8;
    --white: #ffffff;
  }
  * { box-sizing: border-box; margin: 0; padding: 0; }
  html, body { width: 689px; height: 1200px; overflow: hidden; background: var(--cream); }
  .banner {
    position: relative;
    width: 689px;
    height: 1200px;
    background: var(--cream);
    font-family: "Noto Sans", sans-serif;
    color: var(--ink);
    overflow: hidden;
  }
  .brand {
    position: absolute; top: 42px; left: 0; width: 100%;
    text-align: center;
    font-family: "Fraunces", serif; font-weight: 900;
    color: var(--ink);
  }
  .brand-name { font-size: 52px; line-height: 1.02; letter-spacing: -0.5px; }
  .brand-region { font-size: 40px; line-height: 1.1; }
  .headline {
    position: absolute; top: 208px; left: 0; width: 100%;
    text-align: center;
    font-family: "Fraunces", serif; font-weight: 900;
    font-size: 70px; line-height: 1; color: var(--teal);
    letter-spacing: -0.5px;
  }
  .headline-accent {
    position: absolute; top: 282px; left: 0; width: 100%;
    text-align: center;
    font-family: "Fraunces", serif; font-weight: 900;
    font-size: 88px; line-height: 1; color: var(--pink);
    -webkit-text-stroke: 2px var(--pink);
    text-shadow: 0 0 0 var(--white);
    letter-spacing: -2px;
  }
  .slogan-tab {
    position: absolute; top: 392px; left: 50%; transform: translateX(-50%);
    width: 250px; height: 44px;
    background: var(--teal); border-radius: 14px 14px 0 0;
    color: var(--white); text-align: center;
    font-family: "Playfair Display", serif; font-weight: 700;
    font-size: 30px; line-height: 46px;
  }
  .slogan-band {
    position: absolute; top: 434px; left: 0; width: 100%; height: 58px;
    background: var(--teal); color: var(--white); text-align: center;
    font-family: "Playfair Display", serif; font-weight: 700;
    font-size: 42px; line-height: 60px; letter-spacing: -0.5px;
  }
  .tagline {
    position: absolute; top: 506px; left: 0; width: 100%;
    text-align: center; color: var(--teal);
    font-size: 26px; font-weight: 500;
  }
  .services {
    position: absolute; top: 578px; left: 0; width: 100%; height: 322px;
    background: var(--yellow);
  }
  .services-title {
    position: absolute; top: 548px; left: 50%; transform: translateX(-50%);
    width: 300px; height: 58px;
    background: var(--cream); border-radius: 0 0 24px 24px;
    text-align: center; color: var(--pink);
    font-size: 30px; font-weight: 800; line-height: 54px;
  }
  .service-grid {
    position: absolute; top: 612px; left: 40px; width: 609px;
    display: grid; grid-template-columns: repeat(3, 1fr); row-gap: 14px;
  }
  .service { text-align: center; height: 140px; }
  .service-icon {
    display: block; margin: 0 auto 8px;
    width: 84px; height: 84px; border-radius: 50%;
    background: var(--white); border: 6px solid var(--ring);
  }
  .service-label {
    font-size: 19px; font-weight: 800; line-height: 1.05; color: var(--ink);
    letter-spacing: 0.3px;
  }
  .offer-bubble { position: absolute; top: 918px; left: 28px; }
  .offer-text {
    position: absolute; top: 940px; left: 58px; width: 220px;
    text-align: center; color: var(--white);
    font-weight: 800; font-size: 46px; line-height: 0.95;
  }
  .discounts { position: absolute; top: 1050px; left: 48px; }
  .discounts-title { font-size: 23px; font-weight: 800; color: var(--ink); }
  .discounts-list { font-size: 17px; font-weight: 500; color: var(--teal); line-height: 1.25; margin-top: 4px; }
  .mascots {
    position: absolute; top: 905px; left: 380px; width: 285px; height: 240px;
    background: radial-gradient(ellipse at 55% 55%, #d9662a 0%, #c9a58e 45%, rgba(244,237,227,0) 72%);
  }
  .footer {
    position: absolute; top: 1140px; left: 0; width: 100%; height: 60px;
    background: var(--ink); color: var(--white);
    display: flex; align-items: center; gap: 10px; padding-left: 48px;
    font-size: 18px; font-weight: 500;
  }
</style>
</head>
<body>
<main class="banner">
  <header class="brand">
    <div class="brand-name">Willowbrook Critters</div>
    <div class="brand-region">Florida</div>
  </header>

  <h1 class="headline">Professional</h1>
  <div class="headline-accent">PET CARE</div>

  <div class="slogan-tab">For When</div>
  <div class="slogan-band">YOU CAN’T BE THERE</div>

  <p class="tagline">Dog Walking &amp; Pet Sitting</p>

  <section class="services"></section>
  <h2 class="services-title">Our Services</h2>
  <div class="service-grid">
    <div class="service"><span class="service-icon" role="img" aria-label="Icon of a person sitting with a dog"></span><div class="service-label">Extended<br>Visits</div></div>
    <div class="service"><span class="service-icon" role="img" aria-label="Icon of a person with a bin and a dog on a leash"></span><div class="service-label">Pop In<br>Visits</div></div>
    <div class="service"><span class="service-icon" role="img" aria-label="Icon of a car with a paw print"></span><div class="service-label">Pet Taxi</div></div>
    <div class="service"><span class="service-icon" role="img" aria-label="Icon of a person walking a dog"></span><div class="service-label">Dog<br>Walking</div></div>
    <div class="service"><span class="service-icon" role="img" aria-label="Icon of a paw print with an airplane"></span><div class="service-label">Travel</div></div>
    <div class="service"><span class="service-icon" role="img" aria-label="Icon of a hiker with a dog"></span><div class="service-label">Adventure<br>Hikes</div></div>
  </div>

  <svg class="offer-bubble" width="290" height="130" viewBox="0 0 290 130" aria-hidden="true">
    <ellipse cx="140" cy="62" rx="132" ry="60" fill="var(--ink)"/>
    <path d="M230 95 Q250 110 268 126 Q240 122 215 108 Z" fill="var(--ink)"/>
    <path d="M22 40 Q30 14 56 6" fill="none" stroke="var(--ink)" stroke-width="4" stroke-linecap="round"/>
  </svg>
  <div class="offer-text">We<br>offer:</div>

  <div class="discounts">
    <div class="discounts-title">Discounts for</div>
    <div class="discounts-list">First Responders,<br>Teachers, &amp; Military</div>
  </div>

  <div class="mascots" role="img" aria-label="Illustration of a cartoon dog hugging an orange cat"></div>

  <footer class="footer">
    <svg width="18" height="18" viewBox="0 0 20 20" aria-hidden="true">
      <circle cx="10" cy="10" r="8.5" fill="none" stroke="currentColor" stroke-width="1.6"/>
      <ellipse cx="10" cy="10" rx="3.8" ry="8.5" fill="none" stroke="currentColor" stroke-width="1.4"/>
      <line x1="1.5" y1="10" x2="18.5" y2="10" stroke="currentColor" stroke-width="1.4"/>
    </svg>
    <span>www.willowbrookcritters.net</span>
  </footer>
</main>
</body>
</html>
```